Kinsmen Crest Beard Oil Label for 1oz dropper bottle

Create a label for a 1oz beard oil dropper bottle. The label is 1.5 inches tall and 2.75 inches wide. Our logo is listed in the brief so please use it but it doesnt have to be that prominent. BEARD OIL is the most important verbiage. We like elements of all the attached images but we want our own look and feel.

Target Market(s)

Men with beards

Requirements
Must have
• Kinsmen Crest Logo, BEARD OIL, Flavor (Tobacco Vanilla)

Ingredients
Fractionated Coconut Oil (MCT)
Golden Jojoba Oil
Hemp Seed Oil
Tea Tree Essential Oil
Orange Bitter Essential Oil
Peppermint Supreme Essential Oil
Tallow Aromas
DYE FREE

Directions:
Directions: apply 3-6 drops into your hand...rub oil into hands and apply directly onto beard. For best results massage into skin under beard area and work oil out towards beard. Discontinue use if skin becomes irritated.

100% MADE IN THE USA (American Flag 1 color)
Veteran Owned Co.
Nice to have
• Labels can change color with each flavor or a ring can change color to show flavor.

```html
<!DOCTYPE html>
<html lang="en">
<head>
<meta charset="utf-8">
<title>Kinsmen Crest Beard Oil Label</title>
<link href="https://fonts.googleapis.com/css2?family=Pathway+Gothic+One&family=Rye&family=Sancreek&display=swap" rel="stylesheet">
<style>
  :root {
    --backdrop: #a3a3a3;
    --label: #1f1f1f;
    --ink: #ecebe6;
    --gold-light: #f6d27a;
    --gold: #d9a233;
    --gold-deep: #9c6a1b;
  }
  html, body {
    margin: 0;
    width: 1200px;
    height: 1200px;
    overflow: hidden;
    background: var(--backdrop);
  }
  .label {
    position: absolute;
    left: 60px;
    top: 305px;
    width: 1080px;
    height: 590px;
    background: var(--label);
    border-radius: 26px;
    color: var(--ink);
    font-family: "Pathway Gothic One", sans-serif;
  }
  .label-frame {
    position: absolute;
    inset: 22px;
    border: 2px solid var(--ink);
    border-radius: 14px;
  }
  .label-frame::after {
    content: "";
    position: absolute;
    inset: 6px;
    border: 1px solid var(--ink);
    border-radius: 10px;
  }
  .brand-name {
    position: absolute;
    top: 78px;
    left: 0;
    right: 0;
    text-align: center;
    font-size: 40px;
    letter-spacing: 2px;
    line-height: 1;
    color: var(--ink);
  }
  .product-title {
    position: absolute;
    top: 178px;
    left: 0;
    right: 0;
    margin: 0;
    text-align: center;
    font-family: "Sancreek", serif;
    font-weight: 400;
    line-height: 0.95;
    background: linear-gradient(180deg, var(--gold-light) 0%, var(--gold) 50%, var(--gold-deep) 100%);
    -webkit-background-clip: text;
    background-clip: text;
    color: transparent;
  }
  .product-title .word-beard { display: block; font-size: 118px; letter-spacing: 2px; }
  .product-title .word-oil { display: block; font-size: 92px; }
  .flavor {
    position: absolute;
    top: 450px;
    left: 0;
    right: 0;
    display: flex;
    justify-content: center;
    align-items: center;
    gap: 14px;
    font-family: "Rye", serif;
    font-size: 21px;
    letter-spacing: 1px;
  }
  .flavor-rule { width: 28px; height: 20px; }
  .volume {
    position: absolute;
    top: 520px;
    left: 0;
    right: 0;
    text-align: center;
    font-size: 22px;
  }
  .ingredients {
    position: absolute;
    left: 57px;
    top: 158px;
    font-size: 24px;
    line-height: 31px;
  }
  .ingredients h2, .directions h2 {
    margin: 0 0 2px;
    font-weight: 400;
    font-size: 28px;
  }
  .ingredients ul { list-style: none; margin: 0; padding: 0; }
  .directions {
    position: absolute;
    left: 753px;
    top: 95px;
    width: 275px;
    font-size: 22px;
    line-height: 30px;
  }
  .directions p { margin: 0; }
  .made-in-usa {
    position: absolute;
    left: 853px;
    top: 385px;
    width: 100px;
    height: 98px;
    background: var(--ink);
    border: 3px solid var(--label);
    outline: 2px solid var(--ink);
  }
  .veteran {
    position: absolute;
    left: 790px;
    top: 520px;
    width: 225px;
    text-align: center;
    font-size: 23px;
  }
</style>
</head>
<body>
  <section class="label">
    <div class="label-frame"></div>

    <div class="brand-name">Kinsmen Crest</div>

    <h1 class="product-title">
      <span class="word-beard">BEARD</span>
      <span class="word-oil">OIL</span>
    </h1>

    <div class="flavor">
      <svg class="flavor-rule" viewBox="0 0 28 20" aria-hidden="true">
        <g stroke="#ecebe6" stroke-width="1.6">
          <line x1="0" y1="2" x2="28" y2="2"/><line x1="0" y1="7" x2="28" y2="7"/>
          <line x1="0" y1="12" x2="28" y2="12"/><line x1="0" y1="17" x2="28" y2="17"/>
        </g>
      </svg>
      <span>TOBACCO VANILLA</span>
      <svg class="flavor-rule" viewBox="0 0 28 20" aria-hidden="true">
        <g stroke="#ecebe6" stroke-width="1.6">
          <line x1="0" y1="2" x2="28" y2="2"/><line x1="0" y1="7" x2="28" y2="7"/>
          <line x1="0" y1="12" x2="28" y2="12"/><line x1="0" y1="17" x2="28" y2="17"/>
        </g>
      </svg>
    </div>

    <div class="volume">1 fl oz. ( 30ml )</div>

    <div class="ingredients">
      <h2>Ingredients:</h2>
      <ul>
        <li>Fractionated Coconut Oil (MCT)</li>
        <li>Golden Jojoba Oil</li>
        <li>Hemp Seed Oil</li>
        <li>Tea Tree Essential Oil</li>
        <li>Orange Bitter Essential Oil</li>
        <li>Peppermint Supreme Essential Oil</li>
        <li>Tallow Aromas</li>
        <li>DYE FREE</li>
      </ul>
    </div>

    <div class="directions">
      <h2>Directions:</h2>
      <p>Directions: apply 3-6 drops into your hand...rub oil into hands and apply directly onto beard. For best results massage into skin under beard area and work oil out towards beard. Discontinue use if skin becomes irritated.</p>
    </div>

    <div class="made-in-usa" role="img" aria-label="One-colour American flag badge, 100% made in USA"></div>

    <div class="veteran">Veteran Owned Co.</div>
  </section>
</body>
</html>
```